Interior Decoration and Concept Store needs a webpage design

Sophisticated website for my business, name Wren Hollow. Wren Hollow is a design service and homewares store run by interior decorator Marion Tulk.

Marion's qualification and work experience as an interior decorator, is able to provide advice and recommendations for interior and exterior concepts, colour consultations, furniture, lighting, decor concepts and products are sourced for individual projects. A re-upholstery service is also provided.

Facebook icon.
Projects page.
Profile page.
Established 2009
Medial page

Industry/Entity Type

Store

```html
<!DOCTYPE html>
<html lang="en">
<head>
<meta charset="utf-8">
<title>Wren Hollow — Interior Decoration &amp; Concept Store</title>
<link rel="stylesheet" href="https://fonts.googleapis.com/css2?family=Pathway+Gothic+One&family=Arimo:wght@400&family=Jost:wght@400;500&family=Cormorant+Garamond:wght@400&display=swap">
<style>
  :root {
    --brand-red: #d0000f;
    --ink: #1e1e1e;
    --nav-grey: #5e6670;
    --panel-grey: #e4e5e5;
    --field-green: #9cc21a;
    --button-green: #54a62f;
    --footer-dark: #232528;
    --footer-edge: #111214;
    --white: #ffffff;
    --icon-grey: #8a9099;
  }
  * { box-sizing: border-box; margin: 0; padding: 0; }
  html, body { width: 1200px; height: 1099px; overflow: hidden; background: var(--white); }
  .page { position: relative; width: 1200px; height: 1099px; color: var(--ink); font-family: "Arimo", Arial, sans-serif; }
  .abs { position: absolute; }

  /* header */
  .brand { left: 245px; top: 50px; display: flex; align-items: center; gap: 12px; }
  .brand-mark { width: 22px; height: 22px; border-radius: 50%; background: var(--nav-grey); }
  .brand-name { font-family: "Cormorant Garamond", serif; font-size: 44px; color: #2a2a2a; letter-spacing: 1px; }
  .social { top: 16px; display: block; width: 23px; height: 23px; background: var(--icon-grey); }
  .social.first { left: 683px; }
  .social.second { left: 715px; }
  .social.third { left: 747px; }
  .contact { left: 814px; top: 17px; font-family: "Pathway Gothic One", sans-serif; font-size: 16px; color: var(--brand-red); white-space: nowrap; }
  .contact .sep { margin: 0 9px; }
  .main-nav { left: 676px; top: 82px; display: flex; gap: 17px; font-family: "Pathway Gothic One", sans-serif; font-size: 20px; color: var(--nav-grey); }

  /* hero */
  .hero { left: 0; top: 145px; width: 1200px; height: 364px; background: var(--brand-red); }
  .hero-photo { top: 4px; height: 357px; }
  .hero-photo.one { left: 211px; width: 318px; background: linear-gradient(160deg, #f1ece4, #b9ac9c 60%, #8a7d6f); }
  .hero-photo.two { left: 532px; width: 159px; background: linear-gradient(180deg, #efede8 0%, #c7c0b2 45%, #27a8a3 75%, #1a8f8a); }
  .hero-photo.three { left: 695px; width: 317px; background: linear-gradient(180deg, #f4f3f1 0%, #d9d4cc 50%, #6b4a33 85%, #4d3222); }
  .dots { left: 949px; top: 336px; display: flex; gap: 5px; }
  .dot { width: 11px; height: 11px; border-radius: 50%; background: #7b7b7b; }
  .dot.active { background: #111; }

  /* content */
  .section-title { font-family: "Pathway Gothic One", sans-serif; font-size: 29px; font-weight: 400; color: var(--ink); }
  .about-title { left: 184px; top: 552px; }
  .copy { font-size: 10.5px; line-height: 17px; color: #111; text-align: justify; }
  .about-copy { left: 185px; top: 597px; width: 559px; }
  .thumb { top: 740px; width: 211px; height: 101px; }
  .thumb.chair { left: 184px; background: linear-gradient(90deg, #e8ecee 30%, #8b7a2a 55%, #e9e9e7 80%); }
  .thumb.cushions { left: 467px; background: linear-gradient(90deg, #3c3a44 20%, #c9b08a 45%, #e2c23a 65%, #8c8a88); }
  .feature-title { top: 866px; }
  .feature-title.left { left: 173px; }
  .feature-title.right { left: 466px; }
  .feature-copy { top: 905px; }
  .feature-copy.left { left: 173px; width: 261px; }
  .feature-copy.right { left: 466px; width: 290px; }

  /* newsletter */
  .newsletter { left: 789px; top: 550px; width: 288px; height: 291px; background: var(--panel-grey); border-radius: 3px; }
  .newsletter-title { left: 25px; top: 18px; }
  .newsletter-copy { left: 25px; top: 56px; width: 250px; font-family: "Jost", sans-serif; font-size: 12px; line-height: 18.5px; color: #222; }
  .field { left: 31px; width: 187px; height: 42px; border: 2px solid var(--field-green); background: var(--white); font-family: "Arimo", sans-serif; font-size: 14px; color: #9a9a9a; padding: 11px 0 0 13px; }
  .field.user { top: 129px; }
  .field.pass { top: 180px; }
  .login { left: 32px; top: 235px; width: 99px; height: 34px; background: var(--button-green); border-radius: 2px; color: var(--white); font-family: "Jost", sans-serif; font-weight: 500; font-size: 16px; text-align: center; line-height: 34px; }

  /* footer */
  .site-footer { left: 0; top: 1054px; width: 1200px; height: 45px; background: var(--footer-dark); border-top: 2px solid var(--footer-edge); color: #e8e8e8; font-size: 10.5px; text-align: center; line-height: 43px; }
</style>
</head>
<body>
<div class="page">
  <header>
    <div class="abs brand"><span class="brand-mark"></span><span class="brand-name">Wren Hollow</span></div>
    <span class="abs social first" aria-label="Social link"></span>
    <span class="abs social second" aria-label="Social link"></span>
    <span class="abs social third" aria-label="Social link"></span>
    <div class="abs contact">021 555 0148<span class="sep">|</span>hello@wrenhollow.com</div>
    <nav class="abs main-nav"><span>HOME</span><span>PROJECTS</span><span>PROFILE</span><span>ABOUT</span><span>CONTACT US</span></nav>
  </header>

  <section class="abs hero">
    <div class="abs hero-photo one" role="img" aria-label="Photo of a carved timber side table beside a sliding garden door"></div>
    <div class="abs hero-photo two" role="img" aria-label="Photo of framed abstract artwork above a teal chest of drawers"></div>
    <div class="abs hero-photo three" role="img" aria-label="Photo of a timber dining table with black chairs and an orange vase"></div>
    <div class="abs dots"><span class="dot"></span><span class="dot"></span><span class="dot active"></span></div>
  </section>

  <main>
    <h1 class="abs section-title about-title">About Wren Hollow</h1>
    <p class="abs copy about-copy">Lorem ipsum dolor sit amet, consectetur adipiscing elit. Sed at ante. Mauris eleifend, quam a vulputate dictum, massa quam dapibus leo, eget vulputate orci purus ut lorem. In fringilla mi in ligula. Pellentesque aliquam quam vel dolor. Nunc adipiscing. Sed quam odio, tempus ac, aliquam molestie, varius ac, tellus. Vestibulum ut nulla aliquam risus rutrum interdum. Pellentesque lorem. Curabitur sit amet erat quis risus feugiat viverra. Pellentesque augue justo, sagittis et, lacinia at, venenatis non, arcu. Nunc nec libero. In cursus dictum risus. Etiam tristique nisl a nulla. Ut a orci. Curabitur dolor nunc, egestas at, accumsan at, malesuada nec, magna.</p>

    <div class="abs thumb chair" role="img" aria-label="Photo of a mustard upholstered armchair"></div>
    <div class="abs thumb cushions" role="img" aria-label="Photo of patterned cushions on a sofa"></div>

    <h2 class="abs section-title feature-title left">Heading1</h2>
    <p class="abs copy feature-copy left">Lorem ipsum dolor sit amet, consectetur adipiscing elit. Sed at ante. Mauris eleifend, quam a vulputate dictum, massa quam dapibus leo, eget vulputate orci purus ut lorem. In fringilla mi in ligula. Pellentesque aliquam quam vel dolor. Nunc adipiscing. Sed quam odio,</p>
    <h2 class="abs section-title feature-title right">Heading1</h2>
    <p class="abs copy feature-copy right">Lorem ipsum dolor sit amet, consectetur adipiscing elit. Sed at ante. Mauris eleifend, quam a vulputate dictum, massa quam dapibus leo, eget vulputate orci purus ut lorem. In fringilla mi in ligula. Pellentesque aliquam quam vel dolor. Nunc adipiscing. Sed quam odio, tempus ac, aliquam molestie, varius ac, tellus.</p>

    <aside class="abs newsletter">
      <h2 class="abs section-title newsletter-title">Register for Newsletter</h2>
      <p class="abs newsletter-copy">Lorem ipsum dolor sit amet, consectetur adipisicing elit, sed do eiusmod tempor incididunt ut labore et dolore magna aliqua.</p>
      <div class="abs field user">Username</div>
      <div class="abs field pass">Password</div>
      <div class="abs login">Login</div>
    </aside>
  </main>

  <footer class="abs site-footer">Copyright 2014 Wren Hollow - Terms &amp; Conditions | Privacy Policy</footer>
</div>
</body>
</html>
```